Marolina Swimming & Athletics Center

We need Business Card for a Athletics center
The logo frome the Uploaded Files ( b card fimal)
Οn one side of card we need the logo of company the Contact and the website:
1. Address:(Limassol, Cyprus 12-14 Dravelonos str,Ano Feralia,P.C. 5280)

2.Phone number: (+357) 25-804273

3. Mail: info@marolinasport.example

3. Website: www.marolinasport.example

Οn the other side of the card we need to write the sport of the company:

1. Artistic Gymnastics
2. Swimming
3. Gym - Fitness
4. Programs
5. Dancing
5.Tennis

From the Uploaded Files you can get the logo.In a logo is behind the black color which can be removed from logo.

Υou can use that color you want.
.

Industry/Entity Type

Business

Font styles to use
Decorative

Colors
0555a3
ffcf3e
3176b5
0692cd
add136
f04a50
000000
cfcfcf
9d9d9d

Requirements
Should not have
• photos with faces
• photo fro the Website:www.marolinasport.example

```html
<!DOCTYPE html>
<html lang="en">
<head>
<meta charset="utf-8">
<title>Marolina Swimming &amp; Athletics Center — Business Card</title>
<link href="https://fonts.googleapis.com/css2?family=Lato:wght@400;700;900&display=swap" rel="stylesheet">
<style>
  :root {
    --card-dark: #1a1a1a;
    --card-yellow: #ffcf3e;
    --ink: #1b1b1b;
    --gold: #f5b71c;
    --white: #ffffff;
    --page: #e4e6e9;
  }
  * { margin: 0; padding: 0; box-sizing: border-box; }
  html, body { width: 1200px; height: 1200px; overflow: hidden; }
  body {
    background: var(--page);
    font-family: "Lato", sans-serif;
    color: var(--ink);
    position: relative;
  }
  .card {
    position: absolute;
    left: 250px;
    width: 701px;
    height: 401px;
    overflow: hidden;
    box-shadow: 0 14px 30px rgba(0,0,0,0.22);
  }
  .card--front { top: 106px; }
  .card--back { top: 625px; background: var(--card-dark); }

  /* Front */
  .front-brand {
    position: absolute; left: 0; top: 0;
    width: 349px; height: 100%;
    background: var(--card-dark);
  }
  .front-info {
    position: absolute; left: 349px; top: 0;
    width: 352px; height: 100%;
    background: var(--card-yellow);
  }
  .brand-name {
    position: absolute; left: 29px; top: 168px;
    font-weight: 900; font-size: 38px; letter-spacing: 1px;
    color: var(--gold); line-height: 1;
  }
  .brand-mark {
    position: absolute; left: 272px; top: 162px;
    width: 50px; height: 50px; border-radius: 50%;
    border: 3px solid var(--gold);
  }
  .slogan {
    position: absolute; left: 29px; top: 226px;
    font-size: 17.5px; color: var(--white); letter-spacing: 0.1px;
  }
  .holder {
    position: absolute; right: 33px; top: 72px; text-align: right;
  }
  .holder-name { font-size: 29px; font-weight: 400; line-height: 1.05; }
  .holder-role { font-size: 20px; line-height: 1.2; }
  .contact {
    position: absolute; left: 20px; list-style: none;
    display: flex; align-items: flex-start; gap: 10px;
    font-size: 16px; line-height: 20px;
  }
  .contact-icon {
    width: 28px; height: 28px; border-radius: 50%;
    background: var(--ink); flex: none;
    display: flex; align-items: center; justify-content: center;
  }
  .contact-icon svg { width: 16px; height: 16px; }
  .contact--address { top: 173px; }
  .contact--address .contact-icon { margin-top: 3px; }
  .contact--phone { top: 222px; }
  .contact--mail { top: 262px; }
  .contact--web { top: 300px; }
  .contact--phone .contact-text,
  .contact--mail .contact-text,
  .contact--web .contact-text { padding-top: 3px; }

  /* Back */
  .back-name {
    position: absolute; left: 0; right: 0; top: 140px;
    text-align: center;
    font-weight: 900; font-size: 48px; letter-spacing: 2px;
    color: var(--gold);
  }
  .sports-band {
    position: absolute; left: 0; top: 301px;
    width: 100%; height: 71px;
    background: var(--card-yellow);
  }
  .sport {
    position: absolute; font-size: 17px; line-height: 1;
    text-transform: uppercase; white-space: nowrap;
  }
  .sport::before {
    content: ""; position: absolute; left: -18px; top: 5px;
    border-left: 5.5px solid transparent; border-right: 5.5px solid transparent;
    border-top: 9px solid var(--ink);
  }
  .col-1 { left: 62px; }
  .col-2 { left: 295px; }
  .col-3 { left: 500px; }
  .row-1 { top: 17px; }
  .row-2 { top: 44px; }
</style>
</head>
<body>

<section class="card card--front" aria-label="Business card front">
  <div class="front-brand">
    <div class="brand-name">MAROLINA</div>
    <div class="brand-mark" aria-hidden="true"></div>
    <div class="slogan">YOUR AMAZING SLOGAN GOES HERE</div>
  </div>
  <div class="front-info">
    <div class="holder">
      <div class="holder-name">FULL NAME</div>
      <div class="holder-role">Designation</div>
    </div>
    <ul>
      <li class="contact contact--address">
        <span class="contact-icon"><svg viewBox="0 0 16 16"><path d="M8 1.5a4.5 4.5 0 0 0-4.5 4.5C3.5 9.5 8 14.5 8 14.5S12.5 9.5 12.5 6A4.5 4.5 0 0 0 8 1.5z" fill="#ffcf3e"/><circle cx="8" cy="6" r="1.8" fill="#1b1b1b"/></svg></span>
        <span class="contact-text">Limassol, Cyprus 12-14 Dravelonos<br>str,Ano Feralia,P.C. 5280)</span>
      </li>
      <li class="contact contact--phone">
        <span class="contact-icon"><svg viewBox="0 0 16 16"><path d="M4.2 1.8l2 2.6-1.2 1.6c.8 1.9 2.1 3.2 4 4l1.6-1.2 2.6 2-1.2 2.2C7.2 13.2 2.8 8.8 2 3z" fill="#ffcf3e"/></svg></span>
        <span class="contact-text">+357&nbsp; 25-804273</span>
      </li>
      <li class="contact contact--mail">
        <span class="contact-icon"><svg viewBox="0 0 16 16"><rect x="2" y="4" width="12" height="8.5" rx="1" fill="none" stroke="#ffcf3e" stroke-width="1.4"/><path d="M2.5 4.5L8 9l5.5-4.5" fill="none" stroke="#ffcf3e" stroke-width="1.4"/></svg></span>
        <span class="contact-text">info@marolinasport.example</span>
      </li>
      <li class="contact contact--web">
        <span class="contact-icon"><svg viewBox="0 0 16 16" fill="none" stroke="#ffcf3e" stroke-width="1.2"><circle cx="8" cy="8" r="6"/><ellipse cx="8" cy="8" rx="2.6" ry="6"/><path d="M2 8h12M3 5h10M3 11h10"/></svg></span>
        <span class="contact-text">www.marolinasport.example</span>
      </li>
    </ul>
  </div>
</section>

<section class="card card--back" aria-label="Business card back">
  <div class="back-name">MAROLINA</div>
  <div class="sports-band">
    <span class="sport col-1 row-1">Artistic Gymnastics</span>
    <span class="sport col-1 row-2">Swimming</span>
    <span class="sport col-2 row-1">Gym - Fitness</span>
    <span class="sport col-2 row-2">Programs</span>
    <span class="sport col-3 row-1">Dancing</span>
    <span class="sport col-3 row-2">Tennis</span>
  </div>
</section>

</body>
</html>
```